Family Owned General Contracting Business Needs Great E-Flyer Design

We need a one page 8.5"x11" e-flyer type pdf document to use as a marketing and advertising tool. We are a licensed general contractor in Phoenix, Arizona. We target and exclusively work with real estate professionals. The main groups of professionals we target are: real estate investors, real estate agents/property managers, property flippers, commercial and multi family investors, insurance restoration professionals. We are looking for a new e-flyer to specifically market our flooring and custom tile work for showers and kitchen backsplashes. We have been in business for 10+ years, and have an A+ NTR rating. We would like the add to appeal to our target demographic, showcasing some portfolio pictures we have, and have a clean, bright design that's simple and not too busy. We would like to see modern colors used similar to the blue in our logo, and other tones like grays, etc.

I would also like it to include an advertisement for a special price for responding to the ad. The price would be $1.95/sq ft for Installation of ceramic tile up to 20" in size.

We would like it to include our email address, website address, company information, and cell phone to contact. It would be great to incorporate our A+ rating with the National Trade Registry also.

Company Name: Calvaresi Estate Works LLC
Website: http://calvaresiestateworks.example/
Email: works@calvaresiestates.example
Cell: (555)418-7360

I've attached some portfolio pictures of past work we've completed to entice customers to contact us.

Target Market(s)

Real Estate Professionals looking for the flooring and custom tile services from a General Contractor. The main groups of professionals we target are real estate agents, real estate investors, property managers, commercial and multi family investors, property flippers, and insurance restoration professionals.

Industry/Entity Type

Flooring

Number of Pages Required

1 page

Font styles to use
Sans Serif

Colors
3277b5

Requirements
Must have
• We would like it to include our email address, website address, company information, and cell phone to contact. It would be great to incorporate our A+ rating with the National Trade Registry also. We also must have some of the pictures incorporated into the flyer.
• Company Name: Calvaresi Estate Works LLC
• Website: http://calvaresiestateworks.example/
• Email: works@calvaresiestates.example
• Cell: (555)418-7360
Nice to have
• I would also like it to include an advertisement for a special price for responding to the ad. The price would be $1.75/sq ft for Installation of ceramic tile up to 20" in size. Add in that we will provide free estimates.

```html
<!DOCTYPE html>
<html lang="en">
<head>
<meta charset="utf-8">
<title>Calvaresi Estate Works LLC – Flooring &amp; Tile Flyer</title>
<link rel="stylesheet" href="https://fonts.googleapis.com/css2?family=Montserrat:wght@300;400;500;600;700;800&display=swap">
<style>
  :root {
    --brand-blue: #3277b5;
    --bright-blue: #2a9ad6;
    --link-blue: #2f6fb0;
    --ink: #2b2b2b;
    --ink-soft: #3c3c3c;
    --bar-black: #141414;
    --page-bg: #e6e6e6;
    --paper: #ffffff;
    --frame-gray: #7b7b7b;
  }
  * { box-sizing: border-box; margin: 0; padding: 0; }
  html, body { width: 1200px; height: 1200px; overflow: hidden; }
  body {
    background: var(--page-bg);
    font-family: "Montserrat", Arial, sans-serif;
    position: relative;
  }
  .flyer {
    position: absolute;
    left: 226px; top: 71px;
    width: 748px; height: 1058px;
    background: linear-gradient(160deg, #ffffff 0%, #f6f6f6 55%, #efefef 100%);
    box-shadow: 0 4px 14px rgba(0,0,0,.25);
    overflow: hidden;
  }
  .brand {
    position: absolute; left: 44px; top: 58px;
    width: 260px;
    display: flex; align-items: center; gap: 12px;
  }
  .brand-dot {
    width: 38px; height: 38px; border-radius: 50%;
    background: var(--brand-blue);
    flex: none;
  }
  .brand-name {
    font-weight: 600; font-size: 19px; line-height: 1.2;
    color: var(--ink);
  }
  .contact {
    position: absolute; left: 347px; top: 38px;
  }
  .license {
    font-weight: 500; font-size: 19px; color: var(--ink);
    letter-spacing: .5px; margin-bottom: 12px;
  }
  .contact-line {
    display: flex; align-items: center; gap: 5px;
    font-weight: 500; font-size: 14.4px; color: var(--link-blue);
    height: 23px; letter-spacing: .2px;
  }
  .contact-line svg { width: 16px; height: 16px; flex: none; }
  .icon-square { width: 13px; height: 13px; background: var(--ink); border-radius: 2px; margin: 0 2px 0 1px; flex: none; }
  .gallery { position: absolute; left: 0; top: 160px; width: 748px; height: 500px; }
  .highlights {
    position: absolute; left: 50px; top: 671px; width: 660px;
    list-style: none;
    font-weight: 400; font-size: 13.4px; line-height: 19px;
    color: var(--ink-soft); letter-spacing: .2px;
  }
  .highlights li { position: relative; padding-left: 16px; }
  .highlights li::before {
    content: ""; position: absolute; left: 0; top: 5px;
    width: 7px; height: 9px; background: var(--brand-blue);
  }
  .cell-bar {
    position: absolute; left: 0; top: 954px; width: 748px; height: 40px;
    background: var(--bar-black); color: #fff;
    font-weight: 800; font-size: 29px; letter-spacing: 1px;
    display: flex; align-items: center; justify-content: center;
  }
  .offer-bar {
    position: absolute; left: 0; top: 994px; width: 748px; height: 64px;
    background: linear-gradient(90deg, var(--bright-blue), var(--brand-blue));
    color: #fff; text-align: center;
    font-weight: 600; font-size: 13px; line-height: 17px; letter-spacing: .6px;
    padding-top: 12px;
  }
</style>
</head>
<body>
  <main class="flyer">
    <div class="brand">
      <span class="brand-dot"></span>
      <span class="brand-name">Calvaresi Estate<br>Works LLC</span>
    </div>

    <div class="contact">
      <p class="license">ROC #318529</p>
      <p class="contact-line">
        <svg viewBox="0 0 16 16" fill="none" stroke="#2b2b2b" stroke-width="1.3"><circle cx="8" cy="8" r="6.6"/><ellipse cx="8" cy="8" rx="3" ry="6.6"/><path d="M1.4 8h13.2M2.5 4.6h11M2.5 11.4h11"/></svg>
        calvaresiestateworks.example
      </p>
      <p class="contact-line">
        <svg viewBox="0 0 16 16"><rect x="1" y="3" width="14" height="10" fill="#2b2b2b"/><path d="M1 3l7 6 7-6M1 13l5-5M15 13l-5-5" stroke="#fff" stroke-width="1.1" fill="none"/></svg>
        works@calvaresiestates.example
      </p>
      <p class="contact-line">
        <span class="icon-square"></span>
        social.example/calvaresiestateworks
      </p>
    </div>

    <svg class="gallery" viewBox="0 160 748 500">
      <defs>
        <linearGradient id="kitchen" x1="0" y1="0" x2="1" y2="1">
          <stop offset="0" stop-color="#d9d9d6"/><stop offset=".5" stop-color="#bdbdb9"/><stop offset="1" stop-color="#3a3a3a"/>
        </linearGradient>
        <linearGradient id="tileWall" x1="0" y1="0" x2="0" y2="1">
          <stop offset="0" stop-color="#d8d2c8"/><stop offset=".7" stop-color="#cfc7bb"/><stop offset="1" stop-color="#f1efec"/>
        </linearGradient>
        <linearGradient id="patio" x1="0" y1="0" x2="0" y2="1">
          <stop offset="0" stop-color="#7b7a72"/><stop offset=".35" stop-color="#a9a49a"/><stop offset="1" stop-color="#bdbab4"/>
        </linearGradient>
        <linearGradient id="shower" x1="0" y1="0" x2="0" y2="1">
          <stop offset="0" stop-color="#e9e3d6"/><stop offset="1" stop-color="#d4cfc4"/>
        </linearGradient>
      </defs>
      <polygon points="0,216 223,216 183,644 0,644" fill="url(#kitchen)" role="img" aria-label="Photo: renovated kitchen with white cabinets, dark countertop and grey tile backsplash"/>
      <polygon points="183,644 223,216 228,216 190,648 0,648 0,644" fill="var(--brand-blue)"/>
      <polygon points="606,178 748,168 748,600 571,600" fill="url(#shower)" role="img" aria-label="Photo: walk-in shower with white subway tile and glass door"/>
      <polygon points="606,178 748,168 748,174 612,183 577,600 571,600" fill="var(--brand-blue)"/>
      <polygon points="419,218 611,218 563,648 359,638" fill="url(#patio)" role="img" aria-label="Photo: travertine paver patio with stone fountain"/>
      <polygon points="611,218 617,218 568,656 361,646 359,638 563,648" fill="var(--brand-blue)"/>
      <polygon points="227,178 427,168 371,600 187,600" fill="url(#tileWall)" role="img" aria-label="Photo: tiled tub surround with vertical mosaic accent strip"/>
      <polygon points="227,178 427,168 433,166 377,604 371,600 423,174 227,183" fill="var(--brand-blue)"/>
      <polygon points="427,168 433,166 436,164 380,604 377,604" fill="var(--frame-gray)"/>
    </svg>

    <ul class="highlights">
      <li>Calvaresi Estate Works LLC has 10+ year’s experience here in Phoenix.</li>
      <li>Our extensive investing and development background gives us a unique and special insight into what real estate professionals need</li>
      <li>Locally owned family business with an A+ NTR rating and fully licensed and insured.</li>
      <li>We work on all size projects and quality levels, from $100k flip homes to $1m+ custom mansions</li>
      <li>Able to handle a high volume of work with the consistency and quality levels that real estate professionals demand</li>
      <li>We can handle a wide range of projects including: all types of flooring, custom stone work, canterra stone work, paver and driveway/path work, custom tile showers and kitchen backsplashes.</li>
      <li>Customers who work with us typically hire us for our professional quality work that’s always consistent, reliable, and completed on deadline.</li>
      <li>Free estimates</li>
    </ul>

    <div class="cell-bar">Cell: (555)418-7360</div>
    <div class="offer-bar">
      Contact us today and mention this advertisement to receive a special offer for new<br>
      clients: Ceramic floor installation of tile up to 20”x20” 1.75/sq ft.
    </div>
  </main>
</body>
</html>
```